Glow Up by Lakeside 21 day Challenge

We are having a Glow Up by Lakeside Challenge at our fitness studio. We need a poster design using the template attached as a reference. I have also included our Bromalux logo to put on the poster. Please DO NOT use the graphics in the flyer as we are expecting something much better :-)

-Size needed 11x17 with bleeding for printing

-We need this made in Photoshop (CS3 friendly) or at least delivered in PS as we might change some text or re-arrange the design later on.

-We need this in layers.

```html
<!DOCTYPE html>
<html lang="en">
<head>
<meta charset="utf-8">
<title>Glow Up by Lakeside 21 day Challenge</title>
<link rel="stylesheet" href="https://fonts.googleapis.com/css2?family=Anton&family=Roboto+Condensed:ital,wght@0,400;0,700;1,400&display=swap">
<style>
  :root {
    --bg-dark: #0b0b0c;
    --bg-mid: #2a2b2e;
    --gold: #f4c21b;
    --red: #e0231c;
    --white: #ffffff;
    --grey-text: #d8d8d8;
    --panel: rgba(0, 0, 0, 0.82);
    --panel-line: #666;
    --brand-blue: #1e3f8a;
  }
  * { box-sizing: border-box; margin: 0; padding: 0; }
  html, body { width: 778px; height: 1200px; overflow: hidden; background: var(--bg-dark); }
  .poster {
    position: relative;
    width: 778px;
    height: 1200px;
    overflow: hidden;
    font-family: "Roboto Condensed", sans-serif;
    color: var(--white);
    background:
      radial-gradient(ellipse at 50% 18%, #5a5c62 0%, var(--bg-mid) 35%, var(--bg-dark) 75%);
  }
  .hero-photo {
    position: absolute;
    left: 90px; top: 0;
    width: 600px; height: 540px;
    background:
      radial-gradient(ellipse at 50% 30%, #6b4a36 0%, #3d2a20 40%, rgba(20,20,22,0) 72%);
  }
  .headline {
    position: absolute;
    left: 0; right: 0; top: 300px;
    text-align: center;
    font-family: "Anton", sans-serif;
    text-transform: uppercase;
    line-height: 0.98;
    text-shadow: 0 4px 10px rgba(0,0,0,0.75);
  }
  .headline .line-one { display: block; font-size: 84px; color: var(--gold); letter-spacing: 1px; }
  .headline .line-one .accent { color: var(--white); }
  .headline .line-two { display: block; font-size: 112px; color: var(--red); letter-spacing: 1px; }
  .subhead {
    position: absolute;
    left: 0; right: 0; top: 558px;
    text-align: center;
    font-size: 32px;
    line-height: 1.25;
    color: var(--white);
  }
  .subhead .num { color: var(--gold); font-weight: 700; }
  .feature-photo {
    position: absolute;
    left: 230px; top: 648px;
    width: 320px; height: 230px;
    background:
      radial-gradient(ellipse at 50% 40%, #c49a7c 0%, #6e4c3c 32%, rgba(30,30,32,0) 70%);
  }
  .offer-list {
    position: absolute;
    left: 14px; top: 878px;
    width: 750px;
    padding: 7px 12px;
    background: var(--panel);
    border: 1px solid var(--panel-line);
    list-style: none;
    font-size: 15px;
    line-height: 19px;
    color: var(--grey-text);
  }
  .offer-list strong { color: var(--white); }
  .price-line {
    position: absolute;
    left: 0; right: 0; top: 996px;
    text-align: center;
    font-size: 33px;
    line-height: 40px;
    font-weight: 700;
    color: var(--gold);
  }
  .price-line .price { font-size: 40px; }
  .testimonial {
    position: absolute;
    left: 272px; top: 1044px;
    width: 246px;
    padding: 5px 10px;
    background: var(--white);
    color: #222;
    font-size: 13px;
    line-height: 16px;
    font-style: italic;
  }
  .testimonial cite { display: block; text-align: right; font-size: 10px; line-height: 12px; color: #555; }
  .urgency {
    position: absolute;
    left: 18px; top: 1126px;
    width: 240px;
    font-size: 19px;
    font-weight: 700;
    line-height: 1.25;
    color: var(--gold);
    text-transform: uppercase;
  }
  .brand {
    position: absolute;
    left: 272px; top: 1110px;
    width: 246px; height: 70px;
    background: var(--white);
    display: flex;
    align-items: center;
    justify-content: center;
    gap: 10px;
  }
  .brand-dot { width: 18px; height: 18px; border-radius: 50%; background: var(--red); }
  .brand-name { font-size: 32px; font-weight: 700; color: var(--brand-blue); letter-spacing: 1px; }
  .cta {
    position: absolute;
    right: 18px; top: 1134px;
    width: 230px;
    text-align: right;
  }
  .cta-main { font-size: 20px; font-weight: 700; text-transform: uppercase; }
  .cta-contact { font-size: 13px; color: var(--grey-text); margin-top: 4px; }
</style>
</head>
<body>
<main class="poster">
  <div class="hero-photo" role="img" aria-label="Photo of a muscular man in a push-up position in a dark gym"></div>

  <h1 class="headline">
    <span class="line-one">Glow Up <span class="accent">by</span></span>
    <span class="line-two">Lakeside</span>
  </h1>

  <p class="subhead">Discover the Secret to a<br>Beach-Ready Body in Just <span class="num">21</span> Days!</p>

  <div class="feature-photo" role="img" aria-label="Photo of a woman in boxing gloves and sports top"></div>

  <ul class="offer-list">
    <li><strong>9 total</strong> training sessions designed to incinerate fat off your midsection, thighs, and arms</li>
    <li><strong>21 days</strong> of nutritional guidance, including delicious recipes</li>
    <li>A Success Session to map out your individual plan for success</li>
    <li>Your very own Personal Accountability Coach to ensure you get results</li>
  </ul>

  <p class="price-line">You get all this—a $399 value— FOR ONLY <span class="price">$99!</span></p>

  <blockquote class="testimonial">
    I’ve never been more fit in my life—at age 41!
    <cite>—Marlene DuPrell</cite>
  </blockquote>

  <p class="urgency">Hurry! Space is limited to only 20 participants!!!</p>

  <div class="brand">
    <span class="brand-dot"></span>
    <span class="brand-name">BROMALUX</span>
  </div>

  <div class="cta">
    <p class="cta-main">Claim your spot now !</p>
    <p class="cta-contact">Website and Phone Number</p>
  </div>
</main>
</body>
</html>
```